Hold Each Morning As A MOSSbright Harbour

Hello Designers! We need a captivating notebook cover design for our self-development company for people with disabilities. We help people with a diagnosis see everyday as a great adventure than something to ensure. This notebook is to capture the brightness and positivity of everyday, that your struggles are meant for you to overcome. We would like to see designs that follow with our brand (uploaded) and I've also added our logo and kind of notebook as a guide. The final design should be inviting and bright. Use the title "Keep Each Morning A Quiet Lantern". Will decide the words once the background design is finalized

Notebook Size: 8.5 x 5.75 inches
Updates

Hello Designers! I'm extending the deadline to give you an opportunity to submit different and unique designs for the MOSSbright HARBOUR Journal. I've given feedback to most of you so this is your opportunity to try something new. Looking for clean, inviting and unique designs that use the logo colour scheme (attached -- navy blue, light blue, yellow, black). Preferably front and back cover designs.

Target Market(s)

Between 25-35 years

Font styles to use
Serif
Sans Serif
Decorative
Script

Colors
0255a3
fbed22

Requirements
Must have
• -Use colour scheme as per attachment as main colours (can go beyond for contrast ex. pinks/purples/indigo/etc)
Nice to have
• Would like to see designs related to nature, art and/or graphic prints.
Should not have
• icons (no stick figures), silhouettes of people, no hands
• NO stock images

```html
<!DOCTYPE html>
<html lang="en">
<head>
<meta charset="utf-8">
<title>Keep Each Morning A Quiet Lantern — Notebook Cover</title>
<link rel="stylesheet" href="https://fonts.googleapis.com/css2?family=Great+Vibes&display=swap">
<style>
  :root {
    --sky-deep: #0b1230;
    --sky-mid: #1d2a66;
    --sky-violet: #3a3f8f;
    --glow-warm: #ffe9b8;
    --panel-veil: rgba(190, 190, 200, 0.42);
    --ink: #111111;
    --paper: #ffffff;
    --brand-navy: #0255a3;
  }
  html, body {
    margin: 0;
    padding: 0;
    width: 855px;
    height: 1200px;
    overflow: hidden;
    background: var(--paper);
  }
  .cover {
    position: relative;
    width: 855px;
    height: 1200px;
    overflow: hidden;
  }
  .night-sky {
    position: absolute;
    inset: 0;
    background:
      radial-gradient(ellipse 260px 180px at 50% 83%, var(--glow-warm) 0%, rgba(255,233,184,0.35) 30%, rgba(255,233,184,0) 70%),
      linear-gradient(115deg, rgba(90,100,180,0) 35%, rgba(120,120,190,0.35) 50%, rgba(90,100,180,0) 65%),
      linear-gradient(180deg, var(--sky-deep) 0%, var(--sky-mid) 45%, var(--sky-violet) 100%);
  }
  .brand-tag {
    position: absolute;
    left: 338px;
    top: 36px;
    width: 189px;
    height: 99px;
    background: var(--paper);
    display: flex;
    align-items: center;
    justify-content: center;
    font-family: 'Great Vibes', cursive;
    font-size: 48px;
    color: var(--brand-navy);
  }
  .title-veil {
    position: absolute;
    left: 171px;
    top: 178px;
    width: 552px;
    height: 783px;
    background: var(--panel-veil);
  }
  .cover-title {
    position: absolute;
    left: 100px;
    right: 100px;
    top: 200px;
    margin: 0;
    font-family: 'Great Vibes', cursive;
    font-weight: 400;
    font-size: 104px;
    line-height: 1;
    text-align: center;
    color: var(--ink);
    text-shadow: 0 0 2px var(--paper), 2px 2px 0 var(--paper), -1px -1px 0 var(--paper), 3px 4px 6px rgba(255,255,255,0.8);
  }
  .cover-title span {
    position: absolute;
    left: 0;
    right: 0;
    white-space: nowrap;
  }
  .line-1 { top: 20px; }
  .line-2 { top: 175px; font-size: 92px; }
  .line-3 { top: 300px; }
  .line-4 { top: 425px; }
  .line-5 { top: 570px; }
</style>
</head>
<body>
  <main class="cover">
    <div class="night-sky" role="img" aria-label="Starry night sky with the Milky Way above a lit lighthouse tower"></div>
    <div class="brand-tag">Larkwell</div>
    <div class="title-veil"></div>
    <h1 class="cover-title">
      <span class="line-1">Keep</span>
      <span class="line-2">Each Morning</span>
      <span class="line-3">a</span>
      <span class="line-4">Quiet</span>
      <span class="line-5">Lantern</span>
    </h1>
  </main>
</body>
</html>
```